Pellham Ridge Nectar Company, local Honey producer needs product Lable to encourage sales

We are a small business (Pellham Ridge Nectar Company) located in a small Texas town that harvests honey from our beehives yearly. Our honey would be considered "raw wildflower honey" and our goal is to sell it locally (farmers markets) and to surrounding areas.

We are currently packaging in plastic classic honey bottles with white flip caps. Sizes are 8oz and 16oz bottles (see pictures for actual size). Larger orders will be filled in one quart mason jars.

Design Ideas:
-vintage style design with bee or several bees in background
- incorporate company name "Pellham Ridge Nectar Company"
- needs small description "Raw Honey", and "Harvested in Bellville, Texas"

Target Market(s)

Farmers markets, health conscience people looking for unprocessed food options

Industry/Entity Type

Small Business

Requirements
Nice to have
• Vintage feel
Should not have
• No cartoonish characters

```html
<!DOCTYPE html>
<html lang="en">
<head>
<meta charset="utf-8">
<title>Raw Wildflower Honey Label</title>
<link href="https://fonts.googleapis.com/css2?family=Cinzel:wght@400;500&family=Arimo:wght@400;700&family=Tinos&display=swap" rel="stylesheet">
<style>
  :root {
    --page: #ffffff;
    --gold: #d9b36a;
    --gold-light: #f6e2a8;
    --cream: #f7e7c0;
    --red-deep: #7e0a0c;
    --red: #b3160f;
    --orange: #e0601a;
    --band: #0b0b0b;
    --white: #ffffff;
  }
  html, body {
    margin: 0;
    padding: 0;
    width: 1091px;
    height: 1200px;
    overflow: hidden;
    background: var(--page);
  }
  .canvas {
    position: relative;
    width: 1091px;
    height: 1200px;
  }
  .label {
    position: absolute;
    left: 235px;
    top: 125px;
    width: 620px;
    height: 950px;
  }
  .label-shape {
    position: absolute;
    inset: 0;
  }
  .ornament {
    position: absolute;
    left: 250px;
    width: 120px;
    height: 18px;
    border-radius: 9px;
    background: linear-gradient(90deg, transparent, var(--gold-light), transparent);
    opacity: .85;
  }
  .ornament-top { top: 62px; }
  .ornament-bottom { top: 372px; height: 14px; }
  .title {
    position: absolute;
    top: 92px;
    left: 0;
    width: 620px;
    margin: 0;
    text-align: center;
    font-family: "Cinzel", serif;
    font-weight: 400;
    font-size: 70px;
    line-height: 86px;
    color: var(--cream);
    letter-spacing: -1px;
  }
  .company {
    position: absolute;
    top: 408px;
    left: 0;
    width: 620px;
    margin: 0;
    text-align: center;
    font-family: "Arimo", sans-serif;
    font-size: 25px;
    color: var(--white);
  }
  .band-text {
    position: absolute;
    top: 730px;
    left: 0;
    width: 620px;
    text-align: center;
    color: var(--white);
  }
  .band-heading {
    margin: 0;
    font-family: "Tinos", serif;
    font-size: 38px;
    line-height: 48px;
  }
  .band-origin {
    margin: 6px 0 0;
    font-family: "Arimo", sans-serif;
    font-weight: 700;
    font-size: 23px;
    line-height: 32px;
  }
</style>
</head>
<body>
<main class="canvas">
  <section class="label">
    <svg class="label-shape" width="620" height="950" viewBox="0 0 620 950">
      <defs>
        <linearGradient id="goldRim" x1="0" y1="0" x2="1" y2="1">
          <stop offset="0" stop-color="#f6e2a8"/>
          <stop offset=".5" stop-color="#b88a3c"/>
          <stop offset="1" stop-color="#f0d08a"/>
        </linearGradient>
        <radialGradient id="redField" cx=".5" cy=".6" r=".7">
          <stop offset="0" stop-color="#ef7a22"/>
          <stop offset=".45" stop-color="#c42a10"/>
          <stop offset="1" stop-color="#7e0a0c"/>
        </radialGradient>
        <linearGradient id="honeyScene" x1="0" y1="0" x2="0" y2="1">
          <stop offset="0" stop-color="#e2a23a"/>
          <stop offset=".5" stop-color="#f08a1c"/>
          <stop offset="1" stop-color="#c8560e"/>
        </linearGradient>
        <clipPath id="innerClip">
          <rect x="16" y="16" width="588" height="918" rx="294" ry="225"/>
        </clipPath>
      </defs>
      <rect x="2" y="2" width="616" height="946" rx="308" ry="236" fill="url(#goldRim)"/>
      <rect x="10" y="10" width="600" height="930" rx="300" ry="230" fill="#2a0d05"/>
      <g clip-path="url(#innerClip)">
        <rect x="0" y="0" width="620" height="950" fill="url(#redField)"/>
        <rect x="16" y="360" width="90" height="300" fill="#3a0a05" opacity=".55" role="img" aria-label="Bare tree silhouette on the left edge"/>
        <rect x="514" y="360" width="90" height="300" fill="#3a0a05" opacity=".55" role="img" aria-label="Bare tree silhouette on the right edge"/>
        <rect x="16" y="470" width="588" height="238" fill="url(#honeyScene)" role="img" aria-label="Honey dipper dripping over golden honeycomb with mint leaves"/>
        <rect x="0" y="705" width="620" height="245" fill="var(--band)"/>
      </g>
      <rect x="16" y="16" width="588" height="918" rx="294" ry="225" fill="none" stroke="url(#goldRim)" stroke-width="4"/>
    </svg>

    <div class="ornament ornament-top" role="img" aria-label="Gold flourish ornament"></div>
    <h1 class="title">RAW<br>WILDFLOWER<br>HONEY</h1>
    <div class="ornament ornament-bottom" role="img" aria-label="Gold flourish ornament"></div>
    <p class="company">Pellham Ridge Nectar Company</p>

    <div class="band-text">
      <p class="band-heading">RAW HONEY</p>
      <p class="band-origin">Harvested in Bellville,<br>Texas</p>
    </div>
  </section>
</main>
</body>
</html>
```